Bordkarte MY Frelk
Unsere Ideen wurden sehr gut aufgenommen und in der Diskussion weiterentwickelt. Wir freuen uns, das Design einsetzen zu können
Zielgruppe
Bordkarte für ein Rentnerpaar, welches nahezu ganzjährig auf dem eigenen Motorschiff Nord- und Ostsee bereist.
Bei einer Bordkarte stehen Angaben zum Motorschiff im Fokus (Funkkennzeichen Identifikationsnummer)und nicht die des Eignerpaars das maximal mit Vornamen erscheint.
Die Karte wird anderen Eignern abgegeben und dient dazu, dass man sich auch auf grosse Distanzen suchen und kontaktieren kann. So wird bei diesen meist Einzelgängern das soziale Umfeld gepflegt.
Für nicht Berner, 'Frelk' ist Dialekt und bedeutet 'Bär'
Aufgabenstellung
Originelles*, maritimes Sujet oder markantes, nördliches Sternzeichen
(*keine Anker oder Muscheln!)
Maritimes Design, zurückhaltend, repräsentativ.
Die Karte soll das Gefühl der Ruhe und Zufriedenheit vermitteln
Schiff und Namesdesign als Bilder im Anhang. Die Rechte für das Wappen, habe ich einmalig für den Namen erworben.
MY Frelk
Henrike & Olaf
MMSI: 471.803.915
CS: KQRT7
InmarSat : 004926 81037

```html
<!DOCTYPE html>
<html lang="de">
<head>
<meta charset="utf-8">
<title>Bordkarte MY Frelk</title>
<link rel="stylesheet" href="https://fonts.googleapis.com/css2?family=Barlow:wght@800&family=Outfit:wght@700&family=Rye&family=Dancing+Script:wght@700&display=swap">
<style>
  :root {
    --page: #f3f3f3;
    --cream: #fbfaf5;
    --sea: #38a6d6;
    --green: #3aa23d;
    --white: #ffffff;
    --flag-red: #a8121c;
    --flag-dark: #1e1c1d;
    --mist-rose: #dcbcc0;
    --mist-grey: #c6c3c4;
    --glow: #f3e7b8;
  }
  * { margin: 0; padding: 0; box-sizing: border-box; }
  html, body { width: 1200px; height: 1200px; overflow: hidden; }
  body {
    background: var(--page);
    display: flex;
    align-items: center;
    justify-content: center;
    gap: 60px;
  }
  .card {
    position: relative;
    width: 520px;
    height: 336px;
    overflow: hidden;
  }

  /* Front: crest side */
  .card--front {
    background:
      radial-gradient(circle at 50% 45%, var(--glow) 0%, rgba(243,231,184,0) 28%),
      radial-gradient(ellipse at 20% 30%, var(--mist-rose) 0%, var(--mist-grey) 45%, var(--mist-rose) 75%),
      var(--mist-rose);
  }
  .front__name {
    position: absolute;
    left: 50%;
    top: 50%;
    transform: translate(-50%, -50%);
    display: flex;
    align-items: center;
    gap: 12px;
  }
  .front__square {
    width: 26px;
    height: 26px;
    background: var(--flag-red);
  }
  .front__text {
    font-family: "Barlow", sans-serif;
    font-weight: 800;
    font-size: 34px;
    color: var(--flag-dark);
    text-transform: uppercase;
  }

  /* Back: contact side */
  .card--back { background: var(--cream); }
  .back__scene {
    position: absolute;
    left: 0;
    right: 0;
    bottom: 0;
    height: 200px;
    background: linear-gradient(180deg, var(--cream) 0%, #cfe7f2 22%, var(--sea) 48%, var(--sea) 100%);
  }
  .back__label {
    position: absolute;
    left: 243px;
    top: 64px;
    width: 249px;
    height: 30px;
    background: var(--green);
    color: var(--white);
    font-family: "Rye", serif;
    font-size: 15px;
    line-height: 30px;
    text-align: center;
    letter-spacing: 0.5px;
  }
  .back__ids {
    position: absolute;
    right: 28px;
    top: 104px;
    text-align: right;
    font-family: "Outfit", sans-serif;
    font-weight: 700;
    font-size: 15.5px;
    line-height: 23px;
    color: var(--green);
  }
  .back__ship {
    position: absolute;
    left: 36px;
    top: 222px;
    font-family: "Barlow", sans-serif;
    font-weight: 800;
    font-size: 56px;
    line-height: 46px;
    color: var(--white);
    text-transform: uppercase;
  }
  .back__owners {
    position: absolute;
    left: 330px;
    top: 274px;
    font-family: "Dancing Script", cursive;
    font-weight: 700;
    font-size: 19px;
    color: var(--white);
  }
</style>
</head>
<body>
  <section class="card card--front" role="img" aria-label="Vorderseite: weich verlaufendes Flammenmuster in Rot und Schwarz mit Wappen in der Mitte">
    <div class="front__name">
      <span class="front__square"></span>
      <span class="front__text">MY Frelk</span>
    </div>
  </section>

  <section class="card card--back">
    <div class="back__scene" role="img" aria-label="Illustration: blaue Meereswelle mit kleinem Segelboot mit grün-gelbem Rumpf"></div>
    <div class="back__label">HERE'S HOW TO FIND US</div>
    <div class="back__ids">
      <p>MMSI: 471.803.915</p>
      <p>CS: KQRT7</p>
      <p>InmarSat: 004926 81037</p>
    </div>
    <div class="back__ship">MY<br>Frelk</div>
    <div class="back__owners">Henrike &amp; Olaf</div>
  </section>
</body>
</html>
```